Saffron Table signage

Simple design for a new food court outlet: Saffron Table
They serve a fusion of Indian and Mediterranean food and we need signage with fonts and colors that reflect the warmth and spice of the cultures.
The sign is long and skinny. 1 foot tall by 18 feet long.

Target Market(s)

Ski resort guests eating at our base area food court with multiple selections to choose from.

Industry/Entity Type

Court

Requirements
Must have
• Clear readability. Name should be prominent and bright.
Nice to have
• Simple clear text. Possibly use fonts that relate to Indian and Mediterranean inspirations. Warm colors that make you want to eat the food.
Should not have
• Should not have too many graphic elements that it makes it hard to read.

```html
<!DOCTYPE html>
<html lang="en">
<head>
<meta charset="utf-8">
<title>Saffron Table signage</title>
<link rel="stylesheet" href="https://fonts.googleapis.com/css2?family=Yatra+One&family=Cormorant+Garamond:ital,wght@1,600&display=swap">
<style>
  :root {
    --page: #ffffff;
    --band: #ff7f00;
    --frame: #22ff00;
    --name: #6b4f2a;
    --tagline: #2a1a0a;
    --art-top: #3fcf3a;
    --art-bottom: #a8a070;
  }
  * { margin: 0; padding: 0; box-sizing: border-box; }
  html, body {
    width: 1200px;
    height: 900px;
    overflow: hidden;
    background: var(--page);
  }
  .canvas {
    position: relative;
    width: 1200px;
    height: 900px;
  }
  .sign {
    position: absolute;
    left: 0;
    top: 414px;
    width: 1200px;
    height: 71px;
    background: var(--band);
    border: 5px solid var(--frame);
  }
  .sign__art {
    position: absolute;
    top: 1px;
    width: 68px;
    height: 58px;
    background: linear-gradient(to bottom, var(--art-top), var(--art-bottom));
    opacity: 0.55;
  }
  .sign__art--left { left: 33px; }
  .sign__art--right { left: 1087px; }
  .sign__type {
    position: absolute;
    left: 0;
    top: 0;
    width: 1190px;
    height: 61px;
    overflow: visible;
  }
  .sign__name {
    font-family: "Yatra One", "Trebuchet MS", sans-serif;
    font-size: 46px;
    fill: var(--name);
  }
  .sign__cuisine {
    font-family: "Yatra One", "Trebuchet MS", sans-serif;
    font-size: 24px;
    fill: var(--name);
  }
  .sign__tagline {
    font-family: "Cormorant Garamond", Georgia, serif;
    font-style: italic;
    font-weight: 600;
    font-size: 22px;
    fill: var(--tagline);
  }
</style>
</head>
<body>
  <div class="canvas">
    <div class="sign">
      <div class="sign__art sign__art--left" role="img" aria-label="Decorative spice-garden illustration"></div>
      <svg class="sign__type" viewBox="0 0 1190 61" aria-label="Saffron Table, spice kitchen, Spice Up - Sit Down - Dig In">
        <text class="sign__name" x="143" y="55" textLength="314" lengthAdjust="spacingAndGlyphs">SAFFRON TABLE</text>
        <text class="sign__cuisine" x="502" y="44" textLength="159" lengthAdjust="spacingAndGlyphs">spice kitchen</text>
        <text class="sign__tagline" x="767" y="45" textLength="242" lengthAdjust="spacingAndGlyphs">Spice Up - Sit Down - Dig In</text>
      </svg>
      <div class="sign__art sign__art--right" role="img" aria-label="Decorative spice-garden illustration"></div>
    </div>
  </div>
</body>
</html>
```